TRUCKING/TRANSPORTATION COMPANY BUSINESS CARD.

We need a business card design for our trucking company based in Millbrook, AL.
It will be a double sided design.
FRONT SIDE:
We need a good looking logo with a tagline. The tagline should match the type of business.
COMPANY NAME: DW HAULAGE LLC
BACK SIDE:
The following information should be displayed on the back of the card.
Office: 555.274.1968
Mailing: 214 W. Birch Ave.
Millbrook, AL 38921
Email: dwhaulllc@mailbox-example.net
Trucking Company
FRONT SIDE:
BACK SIDE:
Office: 555.274.1968
Mailing: 214 W. Birch Ave.
Millbrook, AL 38921

```html
<!DOCTYPE html>
<html lang="en">
<head>
<meta charset="utf-8">
<title>DW Haulage LLC – Business Card</title>
<link rel="stylesheet" href="https://fonts.googleapis.com/css2?family=Teko:wght@500&family=Alegreya:wght@400&display=swap">
<style>
  :root {
    --frame-yellow: #ffe400;
    --brand-yellow: #ffe500;
    --ink: #1a1a1a;
    --paper: #ffffff;
    --card-border: #2a2a2a;
    --scene-light: #dcdcdc;
    --scene-dark: #8f8f8f;
  }
  html, body {
    margin: 0;
    padding: 0;
    overflow: hidden;
  }
  body {
    width: 1200px;
    height: 1000px;
    background: var(--paper);
  }
  .board {
    position: relative;
    width: 1200px;
    height: 1000px;
    box-sizing: border-box;
    border: 3px solid var(--frame-yellow);
    background: var(--paper);
  }
  .wordmark {
    position: absolute;
    display: flex;
    align-items: center;
    gap: 10px;
    font-family: "Teko", "Arial Narrow", sans-serif;
    font-weight: 500;
    color: var(--ink);
    white-space: nowrap;
    line-height: 1;
  }
  .wordmark .mark-square {
    background: var(--brand-yellow);
    flex: none;
  }
  .hero-mark {
    left: 0;
    width: 1194px;
    top: 100px;
    justify-content: center;
    font-size: 66px;
  }
  .hero-mark .mark-square { width: 40px; height: 40px; }

  .card {
    position: absolute;
    top: 252px;
    width: 314px;
    height: 179px;
    box-sizing: border-box;
    border: 2px solid var(--card-border);
    background: var(--paper);
    overflow: hidden;
  }
  .card-back { left: 259px; }
  .card-front { left: 618px; }

  .card-art {
    position: absolute;
    inset: 0;
  }
  .card-back .wordmark {
    left: 7px;
    top: 24px;
    font-size: 22px;
    gap: 5px;
  }
  .card-back .mark-square { width: 12px; height: 12px; }

  .contact {
    position: absolute;
    right: 5px;
    top: 82px;
    margin: 0;
    padding: 0;
    list-style: none;
    text-align: right;
    font-family: "Alegreya", Georgia, serif;
    font-size: 14px;
    line-height: 22px;
    color: var(--ink);
    white-space: nowrap;
  }

  .card-front .wordmark {
    left: 6px;
    top: 50px;
    font-size: 34px;
    gap: 6px;
  }
  .card-front .mark-square { width: 16px; height: 16px; }
  .company {
    position: absolute;
    right: 7px;
    top: 96px;
    text-align: right;
    font-family: "Teko", "Arial Narrow", sans-serif;
    font-weight: 500;
    color: var(--ink);
    line-height: 1;
    white-space: nowrap;
  }
  .company-name { font-size: 32px; letter-spacing: 0.5px; }
  .company-tagline { font-size: 25px; margin-top: 2px; letter-spacing: 0.3px; }

  .mockup-scene {
    position: absolute;
    left: 275px;
    top: 487px;
    width: 640px;
    height: 428px;
    background: radial-gradient(ellipse at 70% 35%, var(--scene-light), var(--scene-dark));
  }
</style>
</head>
<body>
  <main class="board">
    <div class="wordmark hero-mark">
      <span class="mark-square"></span>
      <span class="mark-name">DW HAULAGE LLC</span>
    </div>

    <section class="card card-back" aria-label="Card back">
      <svg class="card-art" width="310" height="175" viewBox="0 0 310 175" aria-hidden="true">
        <rect x="160" y="39" width="147" height="7" fill="var(--ink)"/>
        <polygon points="0,175 99,104 83,175" fill="var(--brand-yellow)"/>
      </svg>
      <div class="wordmark">
        <span class="mark-square"></span>
        <span class="mark-name">DW HAULAGE LLC</span>
      </div>
      <ul class="contact">
        <li>555.274.1968</li>
        <li>214 W. Birch Ave.</li>
        <li>Millbrook, AL 38921</li>
        <li>dwhaulllc@mailbox-example.net</li>
      </ul>
    </section>

    <section class="card card-front" aria-label="Card front">
      <svg class="card-art" width="310" height="175" viewBox="0 0 310 175" aria-hidden="true">
        <rect x="215" y="73" width="92" height="14" fill="var(--ink)"/>
      </svg>
      <div class="wordmark">
        <span class="mark-square"></span>
        <span class="mark-name">DW HAULAGE</span>
      </div>
      <div class="company">
        <div class="company-name">DW HAULAGE LLC</div>
        <div class="company-tagline">HAULING PROS</div>
      </div>
    </section>

    <div class="mockup-scene" role="img" aria-label="Photo of both printed cards lying on an open notebook beside a pen"></div>
  </main>
</body>
</html>
```